Attorney Business Card

I need a business card that looks professional yet modern. I am an Attorney. , I need a professional yet modern business card for my law practice. My logo and information have been uploaded. , I need a business card that looks professional yet modern. I am an Attorney. , I need a professional yet modern business card for my law practice. My logo and information have been uploaded.

Industry/Entity Type

Business

Requirements
Must have
• My logo which has been uploaded , my logo , My logo which has been uploaded , my logo

```html
<!DOCTYPE html>
<html lang="en">
<head>
<meta charset="utf-8">
<title>Marwood Law Firm – Business Card</title>
<link rel="stylesheet" href="https://fonts.googleapis.com/css2?family=Public+Sans:wght@400;500;600&display=swap">
<style>
  :root {
    --backdrop: #2b2b2b;
    --card-light: #f7f7f5;
    --card-dark: #242424;
    --ink: #1f1f1f;
    --brand-blue: #2d5d8c;
    --silver: #d9d9d9;
    --muted-silver: #bdbdbd;
  }
  * { margin: 0; padding: 0; box-sizing: border-box; }
  html, body {
    width: 1200px;
    height: 900px;
    overflow: hidden;
    background: var(--backdrop);
    font-family: "Public Sans", Arial, sans-serif;
  }
  .canvas { position: relative; width: 1200px; height: 900px; }

  .card {
    position: absolute;
    left: 355px;
    width: 487px;
    height: 270px;
  }
  .card--front { top: 158px; background: var(--card-light); color: var(--ink); }
  .card--back  { top: 467px; background: var(--card-dark); color: var(--silver); }

  .brand {
    position: absolute;
    display: flex;
    flex-direction: column;
    align-items: center;
    text-align: center;
    font-weight: 500;
  }
  .brand__dot {
    width: 58px;
    height: 58px;
    border-radius: 50%;
    border: 2px solid currentColor;
    margin-bottom: 18px;
  }
  .brand__name { font-size: 27px; letter-spacing: 1px; line-height: 1; }
  .brand__sub  { font-size: 14px; letter-spacing: 2px; margin-top: 6px; }

  .card--front .brand { left: 39px; top: 75px; width: 180px; color: var(--brand-blue); }
  .card--back  .brand { left: 266px; top: 75px; width: 180px; color: var(--silver); }

  .contact { position: absolute; left: 283px; top: 43px; font-size: 12.5px; line-height: 16px; }
  .contact__name  { font-size: 15px; font-weight: 600; line-height: 18px; }
  .contact__title { color: var(--brand-blue); margin-bottom: 20px; }
  .contact__lines { list-style: none; margin-bottom: 24px; }
  .contact__label { display: inline-block; width: 19px; color: var(--brand-blue); }

  .website {
    position: absolute;
    left: 60px;
    top: 180px;
    font-size: 12.5px;
    letter-spacing: 1.5px;
    color: var(--muted-silver);
  }
</style>
</head>
<body>
<main class="canvas">
  <section class="card card--front" aria-label="Business card front">
    <div class="brand">
      <span class="brand__dot"></span>
      <span class="brand__name">MARWOOD</span>
      <span class="brand__sub">LAW FIRM</span>
    </div>
    <div class="contact">
      <p class="contact__name">Daniel Marwood, ESQ.</p>
      <p class="contact__title">Attorney at law</p>
      <ul class="contact__lines">
        <li><span class="contact__label">T</span>310.555.0142</li>
        <li><span class="contact__label">F</span>310.555.0187</li>
        <li><span class="contact__label">M</span>310.555.0263</li>
        <li>daniel@mwfirm.com</li>
      </ul>
      <address style="font-style: normal;">
        8120 Crescent Blvd.<br>
        Penthouse<br>
        Westfield, CA 90300
      </address>
    </div>
  </section>

  <section class="card card--back" aria-label="Business card back">
    <p class="website">www.mwfirm.com</p>
    <div class="brand">
      <span class="brand__dot"></span>
      <span class="brand__name">MARWOOD</span>
      <span class="brand__sub">LAW FIRM</span>
    </div>
  </section>
</main>
</body>
</html>
```